Modern Business Card Design Needed for Young Realtor

Information that is going on the card:Marvin Pold
Broker/Owner
555.210.3367
Marvin@MPoldRealty.com
www.MPoldRealty.com

Would also like to include my Instagram Handle somewhere. Probably on the back: the_queencity_realtorMy previous business card is attached, I like that one but would like an updated version and maybe a few design changes

Marvin Pold
Broker/Owner
555.210.3367
Marvin@MPoldRealty.com
www.MPoldRealty.com

• Would also like to include my Instagram Handle somewhere. Probably on the back: the_pinecrest_realtor
• Dorrance Hale or the DH (logo from the previous card.)

```html
<!DOCTYPE html>
<html lang="en">
<head>
<meta charset="utf-8">
<title>MPold Realty – Business Card</title>
<link href="https://fonts.googleapis.com/css2?family=Open+Sans:wght@400;600&family=Oswald:wght@600&display=swap" rel="stylesheet">
<style>
  :root {
    --brand-red: #a91e2f;
    --ink: #2b2b2b;
    --paper: #f5f5f5;
    --backdrop: #e2e2e2;
    --white: #ffffff;
  }
  * { margin: 0; padding: 0; box-sizing: border-box; }
  html, body { width: 1200px; height: 960px; overflow: hidden; }
  body {
    background: var(--backdrop);
    font-family: "Open Sans", Arial, sans-serif;
    position: relative;
  }
  .card {
    position: absolute;
    left: 250px;
    width: 700px;
    height: 400px;
    overflow: hidden;
    box-shadow: 0 6px 18px rgba(0,0,0,0.18);
  }

  /* Back side */
  .card-back {
    top: 50px;
    background: var(--brand-red);
    color: var(--white);
  }
  .card-back .brand-name {
    position: absolute;
    top: 150px;
    width: 100%;
    text-align: center;
    font-size: 44px;
    font-weight: 600;
    line-height: 1.2;
  }
  .social-handle {
    position: absolute;
    top: 300px;
    width: 100%;
    text-align: center;
    font-size: 22px;
    font-weight: 400;
    letter-spacing: 0.5px;
  }

  /* Front side */
  .card-front {
    top: 510px;
    background: var(--paper);
    color: var(--ink);
  }
  .portrait {
    position: absolute;
    inset: 0;
  }
  .front-brand {
    position: absolute;
    top: 96px;
    left: 58px;
    font-size: 32px;
    font-weight: 600;
    line-height: 1.2;
    color: var(--ink);
  }
  .agent-name {
    position: absolute;
    top: 172px;
    left: 58px;
    font-family: "Oswald", "Arial Narrow", sans-serif;
    font-weight: 600;
    font-size: 46px;
    line-height: 1;
    text-transform: uppercase;
  }
  .agent-name .first { color: var(--brand-red); }
  .agent-name .last { color: var(--ink); }
  .agent-title {
    position: absolute;
    top: 230px;
    left: 58px;
    font-size: 22px;
  }
  .contact-list {
    position: absolute;
    top: 280px;
    left: 58px;
    list-style: none;
    font-size: 20px;
  }
  .contact-list li {
    display: flex;
    align-items: center;
    gap: 12px;
    height: 32px;
  }
  .contact-list svg { width: 18px; height: 18px; flex: none; }
  .contact-list .accent { color: var(--brand-red); }
</style>
</head>
<body>

  <section class="card card-back" aria-label="Card back">
    <div class="brand-name">MPold Realty</div>
    <div class="social-handle">the_pinecrest_realtor</div>
  </section>

  <section class="card card-front" aria-label="Card front">
    <svg class="portrait" width="700" height="400" viewBox="0 0 700 400">
      <defs>
        <linearGradient id="portraitTone" x1="0" y1="0" x2="1" y2="1">
          <stop offset="0" stop-color="#6f9a4c"/>
          <stop offset="0.5" stop-color="#a6a89a"/>
          <stop offset="1" stop-color="#5f6064"/>
        </linearGradient>
      </defs>
      <path role="img" aria-label="Portrait photo of the broker in a grey blazer, garden behind"
            d="M700 0 L420 0 C330 130 360 300 520 400 L700 400 Z"
            fill="url(#portraitTone)"/>
      <path d="M420 0 C330 130 360 300 520 400" fill="none" stroke="#a91e2f" stroke-width="5"/>
    </svg>

    <div class="front-brand">MPold Realty</div>

    <h1 class="agent-name"><span class="first">Marvin</span> <span class="last">Pold</span></h1>
    <p class="agent-title">Broker/Owner</p>

    <ul class="contact-list">
      <li>
        <svg viewBox="0 0 24 24"><path fill="#a91e2f" d="M6.6 10.8a15 15 0 0 0 6.6 6.6l2.2-2.2a1 1 0 0 1 1-.25 11.4 11.4 0 0 0 3.6.57 1 1 0 0 1 1 1V20a1 1 0 0 1-1 1A17 17 0 0 1 3 4a1 1 0 0 1 1-1h3.5a1 1 0 0 1 1 1c0 1.250.2 2.450.57 3.6a1 1 0 0 1-.25 1z"/></svg>
        <span>555.210.3367</span>
      </li>
      <li>
        <svg viewBox="0 0 24 24"><rect x="2" y="5" width="20" height="14" fill="#a91e2f"/><path d="M2 5l10 8 10-8" fill="none" stroke="#fff" stroke-width="1.6"/></svg>
        <span>Marvin@MPoldRealty.com</span>
      </li>
      <li>
        <svg viewBox="0 0 24 24"><circle cx="12" cy="12" r="10" fill="#a91e2f"/><path d="M2 12h20M12 2c3 3 3 17 0 20M12 2c-3 3-3 17 0 20" fill="none" stroke="#fff" stroke-width="1.4"/></svg>
        <span>www.<span class="accent">MPoldRealty</span>.com</span>
      </li>
    </ul>
  </section>

</body>
</html>
```